Business card design needed

I need a business card for my new business.
I make environmentally friendly candles from all natural premium ingredients.
The candles are hand-poured locally in Kestrel Bay, Arvonia.
I also want my card to match my website www.velmirawicks.com.au (similar colours, font). Can add additional fonts to create more interest...
I want my design to reflect class and simplicity.
Target Market(s)
Target audience 25-50
The candles represent luxury but need to appeal to the environmentally conscious...
Needs to appeal to both men and women. A luxury gift a man would buy for his girlfriend or mother or for his home and for a woman it needs to represent quality...
Industry/Entity Type
Business
Contact Information for Business Card
Velmira Candles
Hand-Poured Eco Soy Candles
Lorraine Quibell - Founder
0438 276 904
www.velmirawicks.com.au
Logo Text
VELMIRA
Logo styles of interest
Wordmark Logo
Look and feel
Each slider illustrates characteristics of the customer's brand and the style your logo design should communicate.

```html
<!DOCTYPE html>
<html lang="en">
<head>
<meta charset="utf-8">
<title>Velmira Candles – Business Card</title>
<link rel="stylesheet" href="https://fonts.googleapis.com/css2?family=Arvo:wght@400;700&display=swap">
<style>
  :root {
    --paper: #ffffff;
    --mist-blue: #d3ebef;
    --ink: #333333;
  }
  * { margin: 0; padding: 0; box-sizing: border-box; }
  html, body {
    width: 1200px;
    height: 664px;
    overflow: hidden;
    background: var(--paper);
  }
  .card {
    position: relative;
    width: 1200px;
    height: 664px;
    background: var(--paper);
    color: var(--ink);
    font-family: "Arvo", "Rockwell", serif;
  }
  .brand-name {
    position: absolute;
    top: 40px;
    left: 0;
    width: 100%;
    text-align: center;
    font-size: 78px;
    font-weight: 400;
    letter-spacing: 0.27em;
    padding-left: 0.27em;
    line-height: 1;
    white-space: nowrap;
  }
  .info-band {
    position: absolute;
    top: 171px;
    left: 0;
    width: 100%;
    height: 413px;
    background: var(--mist-blue);
  }
  .tagline {
    position: absolute;
    top: 30px;
    width: 100%;
    text-align: center;
    font-size: 33px;
    letter-spacing: 0.3em;
    padding-left: 0.3em;
    line-height: 1;
    white-space: nowrap;
  }
  .person {
    position: absolute;
    top: 142px;
    left: 240px;
    width: 700px;
  }
  .person-name {
    text-align: center;
    font-size: 57px;
    font-weight: 700;
    letter-spacing: 0.2em;
    padding-left: 0.2em;
    line-height: 1;
    white-space: nowrap;
  }
  .person-role {
    text-align: right;
    margin-top: 8px;
    font-size: 36px;
    letter-spacing: 0.18em;
    line-height: 1;
  }
  .contact {
    position: absolute;
    width: 100%;
    text-align: center;
    font-size: 30px;
    letter-spacing: 0.26em;
    padding-left: 0.26em;
    line-height: 1;
    white-space: nowrap;
  }
  .contact strong { font-weight: 700; }
  .contact-primary { top: 308px; }
  .contact-address { top: 359px; }
  .contact .gap { display: inline-block; width: 18px; }
  .website {
    position: absolute;
    top: 606px;
    width: 100%;
    text-align: center;
    font-size: 34px;
    letter-spacing: 0.32em;
    padding-left: 0.32em;
    line-height: 1;
    white-space: nowrap;
  }
</style>
</head>
<body>
  <main class="card">
    <h1 class="brand-name">VELMIRA CANDLES</h1>
    <section class="info-band">
      <p class="tagline">HAND-POURED ECO SOY CANDLES</p>
      <div class="person">
        <p class="person-name">Lorraine Quibell</p>
        <p class="person-role">Founder</p>
      </div>
      <p class="contact contact-primary">P:<strong>0438 276 904</strong><span class="gap"></span>E:<strong>quibell@velmirawicks.com</strong></p>
      <p class="contact contact-address">A:<strong>Velmira Candles, Kestrel Bay, Arvonia</strong></p>
    </section>
    <p class="website">www.velmirawicks.com.au</p>
  </main>
</body>
</html>
```